Letterhead LOGO and Business Card

Two Projects
1. Logo
2. Logo with Name - Brackley Asset Management for letterhead/business card
This startup is a traditional money manager that offers great value to its clients through professional money management at a very attractive fee structure.

Possible thought/concept 1: Strength, Financial Security/Integrity
Possible layout: Square logo with dark green border (back of $1 bill green), embossed lines like on $1bill (Fairbrook's forehead) in green in relief in background, gold leaf W centered in square (see Corvane Logo) with 5 point stars above the points of the W.
Possible thought/concept 2: Some iteration of a globe and the capital letter W - superimposed, cut-out, etc. This business will have a global presence.
Concept 3: I am not sure if Concept 1 can be blended with Concept 2, but someone out there may be crafty enough to blend the two concepts. If so, make sure China and the US are represented..

Business

W

```html
<!DOCTYPE html>
<html lang="en">
<head>
<meta charset="utf-8">
<title>Brackley Asset Management – Stationery</title>
<link rel="stylesheet" href="https://fonts.googleapis.com/css2?family=Lora:wght@400;700&family=Open+Sans:wght@400&display=swap">
<style>
  :root{
    --bg:#eeeff1;
    --paper:#ffffff;
    --ink:#1f1f1f;
    --ink-soft:#555a60;
    --brand-green:#6cb33f;
    --tint:#e7eef8;
    --shadow:0 6px 18px rgba(0,0,0,.12);
  }
  *{box-sizing:border-box;margin:0;padding:0}
  html,body{width:1200px;height:1000px;overflow:hidden;background:var(--bg)}
  .canvas{position:relative;width:1200px;height:1000px}

  /* wordmark: name set in the text face, one weight, one colour */
  .wordmark{display:flex;align-items:center;gap:10px;color:var(--ink);font-family:"Lora",serif;font-weight:400;line-height:1.15}
  .wordmark__square{flex:none;background:var(--brand-green)}
  .wordmark__name{display:block}

  /* letterhead */
  .letterhead{position:absolute;left:60px;top:100px;width:560px;height:800px;background:var(--paper);box-shadow:var(--shadow);
    padding:46px 52px;font-family:"Lora",serif;color:var(--ink);overflow:hidden}
  .letterhead__tint{position:absolute;right:-80px;top:230px;width:420px;height:420px;border-radius:50%;
    background:radial-gradient(circle,var(--tint) 0%,rgba(231,238,248,0) 70%)}
  .letterhead .wordmark__square{width:12px;height:12px}
  .letterhead .wordmark__name{font-size:18px}
  .letter{position:relative;margin-top:48px;font-size:11.5px;line-height:1.6}
  .letter__date{font-weight:700;font-size:12.5px;margin-bottom:30px}
  .letter__recipient{margin-bottom:20px;color:#333}
  .letter__body p{margin-bottom:14px;color:#333}
  .letter__sign{margin-top:28px;display:flex;align-items:flex-end;gap:14px}
  .signature{width:120px;height:48px;background:linear-gradient(90deg,#f3f3f3,#e6e6e6);border-radius:4px}
  .letter__signer strong{display:block;font-size:13px}
  .letterhead__footer{position:absolute;right:52px;bottom:40px;text-align:right;font-family:"Open Sans",sans-serif;font-size:8.5px;line-height:1.6;color:var(--ink-soft)}

  /* cards */
  .card{position:absolute;width:350px;height:200px;background:var(--paper);box-shadow:var(--shadow);font-family:"Lora",serif;color:var(--ink)}
  .card--back{left:700px;top:100px;padding:32px 30px}
  .card--front{left:700px;top:330px;display:flex;align-items:center;justify-content:center}
  .card--front .wordmark__square{width:12px;height:12px}
  .card--front .wordmark__name{font-size:19px}
  .card__name{font-size:17px}
  .card__role{font-size:10px;color:var(--ink-soft);margin-bottom:40px}
  .card__contact{font-family:"Open Sans",sans-serif;font-size:9.5px;line-height:1.7;color:var(--ink-soft)}

  /* brand name lockup */
  .lockup{position:absolute;left:720px;top:700px;width:440px;height:200px;display:flex;align-items:center;justify-content:center}
  .lockup .wordmark{gap:16px}
  .lockup .wordmark__square{width:22px;height:22px}
  .lockup .wordmark__name{font-size:34px}
</style>
</head>
<body>
<main class="canvas">

  <article class="letterhead">
    <div class="letterhead__tint"></div>
    <header class="wordmark">
      <span class="wordmark__square"></span>
      <span class="wordmark__name">Brackley Asset Management</span>
    </header>

    <section class="letter">
      <p class="letter__date">Port Averly, October 31, 2013</p>
      <p class="letter__recipient">Sr.<br>TOMAS RIVERA<br>Web Master<br>City</p>
      <div class="letter__body">
        <p>Lorem ipsum dolor sit amet,:</p>
        <p>Consetetur sadipscing elitr, sed diam nonumy eirmod tempor invidunt ut labore et dolore magna aliquyam erat, sed diam voluptua. At vero eos et accusam et justo duo dolores et ea rebum. Stet clita kasd gubergren, ipsum dolor sit amet. Lorem ipsum dolor sit amet, consetetur sadipscing elitr, sed diam nonumy eirmod tempor invidunt ut labore et dolore magna aliquyam erat, sed diam voluptua.</p>
        <p>Sed diam nonumy eirmod tempor invidunt ut labore et dolore magna aliquyam erat. At vero eos et accusam et justo duo dolores et ea rebum. Stet clita kasd gubergren, no sea takimata sanctus est sed diam nonumy eirmod tempor invidunt ut labore et dolore magna aliquyam erat, sed diam voluptua.</p>
      </div>
      <div class="letter__sign">
        <div class="signature" role="img" aria-label="Handwritten signature"></div>
        <p class="letter__signer"><strong>ELENA MARSH</strong>Manager</p>
      </div>
    </section>

    <footer class="letterhead__footer">
      www.brackleyam.com, office@brackleyam.com<br>
      Harlow Street 48<br>
      +01 (555) 014-2290, (555) 014-2291<br>
      State, Town, Country
    </footer>
  </article>

  <div class="card card--back">
    <p class="card__name">Elena Marsh</p>
    <p class="card__role">Manager</p>
    <p class="card__contact">office@brackleyam.com<br>+01 (555) 014-2290<br>Harlow Street 48, Port Averly</p>
  </div>

  <div class="card card--front">
    <div class="wordmark">
      <span class="wordmark__square"></span>
      <span class="wordmark__name">Brackley Asset Management</span>
    </div>
  </div>

  <div class="lockup">
    <div class="wordmark">
      <span class="wordmark__square"></span>
      <span class="wordmark__name">Brackley<br>Asset Management</span>
    </div>
  </div>

</main>
</body>
</html>
```